Silver Creek Plumbing Business card & letter head design

We need a new business card and letter head for our plumbing company called silver creek plumbing. attached is the companys logo. We provide domestic and commercial plumbing services in regional western Australia. We are after Something simple yet nice to look at and something that fits within the trade industry.

Target Market(s)

trade/building industry

Contact Information for Business Card

Darl Hensby
Manager
0461 238 574
enquiries@scplumbwork.net.au
ABN: 47 381 905 462
PCL: 5187

Domestic & Commercial Plumbing
Tip Truck & Excavator hire

Colors

Designer to choose colors to be used in the design.

```html
<!DOCTYPE html>
<html lang="en">
<head>
<meta charset="utf-8">
<title>Silver Creek Plumbing – Business Card</title>
<link rel="stylesheet" href="https://fonts.googleapis.com/css2?family=Montserrat:wght@700;800&family=Arimo:wght@400&display=swap">
<style>
  :root {
    --page-bg: #e9ebee;
    --card-bg: #ffffff;
    --brand-blue: #2f78bd;
    --rule-grey: #5b5d60;
    --text-dark: #3c3c3c;
    --card-shadow: rgba(20, 30, 45, 0.18);
  }
  * { margin: 0; padding: 0; box-sizing: border-box; }
  html, body {
    width: 1200px;
    height: 1000px;
    overflow: hidden;
    background: var(--page-bg);
  }
  .canvas {
    position: relative;
    width: 1200px;
    height: 1000px;
  }
  .card {
    position: absolute;
    left: 250px;
    width: 700px;
    height: 400px;
    background: var(--card-bg);
    box-shadow: 0 8px 28px var(--card-shadow);
    overflow: hidden;
  }
  .card--front { top: 70px; }
  .card--back { top: 530px; }

  .card__rule {
    position: absolute;
    left: 0;
    right: 0;
    bottom: 80px;
    height: 4px;
    background: var(--rule-grey);
  }
  .card__band {
    position: absolute;
    left: 0;
    right: 0;
    bottom: 0;
    height: 68px;
    background: var(--brand-blue);
  }

  .brand {
    display: flex;
    align-items: center;
    gap: 12px;
  }
  .brand__dot {
    width: 18px;
    height: 18px;
    border-radius: 50%;
    background: var(--brand-blue);
    flex: none;
  }
  .brand__name {
    font-family: "Montserrat", sans-serif;
    font-weight: 800;
    color: var(--brand-blue);
    text-transform: uppercase;
    line-height: 1.05;
    letter-spacing: 0.5px;
  }

  .card--front .brand {
    position: absolute;
    top: 100px;
    left: 0;
    right: 0;
    justify-content: center;
  }
  .card--front .brand__name { font-size: 34px; }

  .card--back .brand {
    position: absolute;
    top: 128px;
    left: 44px;
    width: 300px;
  }
  .card--back .brand__name { font-size: 27px; }

  .contact {
    position: absolute;
    top: 66px;
    left: 372px;
    font-family: "Arimo", sans-serif;
    color: var(--text-dark);
  }
  .contact__name {
    font-family: "Montserrat", sans-serif;
    font-weight: 700;
    font-size: 22px;
    color: var(--brand-blue);
  }
  .contact__role {
    font-family: "Montserrat", sans-serif;
    font-weight: 700;
    font-size: 13px;
    letter-spacing: 0.6px;
    color: var(--text-dark);
    margin-bottom: 10px;
  }
  .contact__list {
    list-style: none;
    border-left: 3px solid var(--rule-grey);
    padding-left: 12px;
  }
  .contact__item {
    display: flex;
    align-items: center;
    gap: 12px;
    font-size: 16px;
    height: 30px;
  }
  .contact__icon {
    width: 22px;
    height: 22px;
    flex: none;
  }
  .contact__item--plain { padding-left: 34px; }
</style>
</head>
<body>
<main class="canvas">

  <section class="card card--front" aria-label="Business card front">
    <div class="brand">
      <span class="brand__dot"></span>
      <span class="brand__name">Silver Creek Plumbing</span>
    </div>
    <div class="card__rule"></div>
    <div class="card__band"></div>
  </section>

  <section class="card card--back" aria-label="Business card back">
    <div class="brand">
      <span class="brand__dot"></span>
      <span class="brand__name">Silver Creek<br>Plumbing</span>
    </div>

    <div class="contact">
      <p class="contact__name">Darl Hensby</p>
      <p class="contact__role">MANAGER</p>
      <ul class="contact__list">
        <li class="contact__item">
          <svg class="contact__icon" viewBox="0 0 22 22" aria-hidden="true">
            <rect width="22" height="22" fill="#2f78bd"/>
            <rect x="7" y="4" width="8" height="14" rx="1.5" fill="none" stroke="#fff" stroke-width="1.6"/>
            <line x1="10" y1="15.5" x2="12" y2="15.5" stroke="#fff" stroke-width="1.4"/>
          </svg>
          <span>0461 238 574</span>
        </li>
        <li class="contact__item">
          <svg class="contact__icon" viewBox="0 0 22 22" aria-hidden="true">
            <rect width="22" height="22" fill="#2f78bd"/>
            <rect x="4" y="6" width="14" height="10" fill="none" stroke="#fff" stroke-width="1.6"/>
            <polyline points="4,6 11,12 18,6" fill="none" stroke="#fff" stroke-width="1.6"/>
          </svg>
          <span>enquiries@scplumbwork.net.au</span>
        </li>
        <li class="contact__item">
          <svg class="contact__icon" viewBox="0 0 22 22" aria-hidden="true">
            <rect width="22" height="22" fill="#2f78bd"/>
            <rect x="4" y="5" width="14" height="9" fill="none" stroke="#fff" stroke-width="1.6"/>
            <line x1="11" y1="14" x2="11" y2="17" stroke="#fff" stroke-width="1.6"/>
            <line x1="7.5" y1="17.5" x2="14.5" y2="17.5" stroke="#fff" stroke-width="1.6"/>
          </svg>
          <span>www.scplumbwork.net.au</span>
        </li>
        <li class="contact__item contact__item--plain">ABN: 47 381 905 462</li>
        <li class="contact__item contact__item--plain">PCL: 5187</li>
      </ul>
    </div>

    <div class="card__rule"></div>
    <div class="card__band"></div>
  </section>

</main>
</body>
</html>
```